Lamp Across Borders- a non profit locin TZ , east Africa. Needing to attract donors.

A flyer for donors /potential partners. showing what their giving has accomplished this year. An Encouraging way to say thank you at the same time informing the partner of the amazing things God is doing with their generous, faithful giving. We will need to print/email. Thank you for considering this project. Your efforts help in educating and feeding 225 street children, providing a safe haven and trade school for hundreds of women and abused teenagers, medical ship on the longest lake in the world going into unreached people groups, a Bible College Training up pastors to plant churches all over TZ, Congo, Burundi and beyond, youth and children’s kids clubs and youth camps. These are the main areas of lamp across borders. Bible college, primary school, trade schools, youth camps/kids clubs. We need help in making sure readers will be drawn to seeing/reading more which leads to donations without overwhelming with too much info. HELP! I can tell you about Jesus I have even authored 7 books, but making s flyer that makes sense it out of my wheelhouse. Again, thank you.
Updates

I do not want longer I need quicker and paid for a 3 day quote. All pictures and logo are on our website. I have tried to send pictures but they won’t send. Please look at. Www.lampacrossborderstz-example.org

Target Market(s)

Professional adults, large companies, donors

Industry/Entity Type

Non profit missionary Lamp Across Borders in Tanzania, Congo, USA and soon to be Canada.

Requirements
Must have
• Color professional pictures, feel good, exciting want to be apart of what God is doing
Nice to have
• Glossy trifold
Should not have
• Fly in the face, guilt feeling, animals in Africa

```html
<!DOCTYPE html>
<html lang="en">
<head>
<meta charset="utf-8">
<title>Lamp Across Borders – How We Serve</title>
<link rel="stylesheet" href="https://fonts.googleapis.com/css2?family=Oswald:wght@400;500&family=Roboto+Condensed:wght@400;700&family=Playfair+Display+SC:wght@400&display=swap">
<style>
:root{
  --green:#a9bf35;
  --green-soft:#dfe7b4;
  --dark:#262524;
  --dark-2:#34322f;
  --ink:#2f2f2f;
  --white:#ffffff;
  --photo-red:#b8473f;
}
*{box-sizing:border-box;margin:0;padding:0}
html,body{width:1200px;height:932px;overflow:hidden;background:#fff}
.flyer{position:relative;width:1200px;height:932px;overflow:hidden;background:var(--white);font-family:"Roboto Condensed",sans-serif;color:var(--ink)}

/* left column */
.college{position:absolute;left:0;top:0;width:398px;height:932px;background:linear-gradient(90deg,var(--dark) 0%,var(--dark-2) 50%,var(--dark) 100%)}
.campus-photo{position:absolute;left:0;top:0;width:398px;height:236px;background:linear-gradient(180deg,#c9ccc8 0%,#9ea3a0 55%,#5d7a3d 100%)}
.college-name{position:absolute;left:0;top:238px;width:398px;text-align:center;font-family:"Playfair Display SC",serif;font-size:17px;letter-spacing:.5px;color:var(--white)}
.college-wordmark{position:absolute;left:0;top:282px;width:398px;text-align:center;font-family:"Roboto Condensed",sans-serif;font-weight:400;font-size:26px;color:var(--white)}
.college-title{position:absolute;left:20px;top:340px;width:360px;text-align:center;font-family:"Oswald",sans-serif;font-weight:500;font-size:20px;line-height:24px;color:var(--green);text-transform:uppercase}
.college-text{position:absolute;left:20px;top:404px;width:362px;font-size:13.4px;line-height:16.6px;color:var(--white);text-align:justify}
.college-text p{margin-bottom:16px}
.graduation-photo{position:absolute;left:0;top:662px;width:398px;height:270px}

/* right area */
.classroom-photo{position:absolute;left:398px;top:0;width:802px;height:486px}
.serve-heading{position:absolute;left:430px;top:470px;font-family:"Oswald",sans-serif;font-size:24px;font-weight:400;color:var(--ink);text-transform:uppercase;letter-spacing:.3px}
.service{position:absolute;width:368px}
.service h3{display:flex;align-items:center;gap:8px;font-family:"Oswald",sans-serif;font-weight:500;font-size:17px;color:var(--ink);text-transform:uppercase;margin-bottom:6px}
.service h3 svg{flex:none}
.service p{font-size:13.4px;line-height:16.6px;text-align:justify;font-weight:700;color:var(--ink)}
.school{left:430px;top:518px}
.kids{left:430px;top:690px}
.village{left:820px;top:518px;width:356px}
.trade{left:820px;top:690px;width:356px}

.donate-band{position:absolute;left:0;top:0;width:1200px;height:932px}
.donate-title{position:absolute;right:28px;top:842px;font-family:"Oswald",sans-serif;font-weight:500;font-size:22px;color:var(--green);text-transform:uppercase;letter-spacing:.3px}
.donate-site{position:absolute;right:28px;top:883px;display:flex;align-items:center;gap:6px;font-weight:700;font-size:16px;color:var(--white)}
</style>
</head>
<body>
<main class="flyer">

  <aside class="college">
    <div class="campus-photo" role="img" aria-label="Photo of the Bible college campus buildings with a lawn in front"></div>
    <div class="college-name">Lamp Across Borders Bible College</div>
    <div class="college-wordmark">Lamp Across Borders</div>
    <h2 class="college-title">Train Pastors &amp; Plant<br>Churches Through Scholarships</h2>
    <div class="college-text">
      <p>In 2007 we started our first Bible classes in a rented house. The house served as the dorm for men, and we built a grass-roofed pavilion in the yard for our classroom. Unfortunately, we had to limit enrolment to 40 students due to a lack of space.</p>
      <p>Today we have a new campus that can hold over 100 students with housing for both men and women. Pastors and church leaders are trained to go out and plant new churches and ministries. We now have graduates serving all over Tanzania and in DRC (Congo).</p>
      <p>We are affiliated with Harborview Bible Institute in the USA and accept students who would like to study abroad to get a feel for the mission field. Credits earned at LABC transfer to HBI in the states.</p>
    </div>
    <svg class="graduation-photo" viewBox="0 0 398 270" role="img" aria-label="Photo of graduates in caps and gowns at the college graduation ceremony">
      <defs>
        <linearGradient id="gradPhoto" x1="0" y1="0" x2="0" y2="1">
          <stop offset="0" stop-color="#6b6f74"/>
          <stop offset=".6" stop-color="#2c2c2e"/>
          <stop offset="1" stop-color="#4f6a32"/>
        </linearGradient>
      </defs>
      <path d="M0 14 Q100 -4 200 10 T398 4 L398 270 L0 270 Z" fill="url(#gradPhoto)"/>
      <path d="M0 14 Q100 -4 200 10 T398 4" fill="none" stroke="var(--white)" stroke-width="4"/>
      <path d="M0 20 Q100 2 200 16 T398 10" fill="none" stroke="var(--green)" stroke-width="3"/>
    </svg>
  </aside>

  <svg class="classroom-photo" viewBox="0 0 802 486" role="img" aria-label="Photos of primary school children in red uniforms in class, children worshipping, and a woman sewing at the trade school">
    <defs>
      <linearGradient id="classPhoto" x1="0" y1="0" x2="1" y2="1">
        <stop offset="0" stop-color="#9aa39c"/>
        <stop offset=".45" stop-color="var(--photo-red)"/>
        <stop offset="1" stop-color="#5d4a3a"/>
      </linearGradient>
      <linearGradient id="worshipPhoto" x1="0" y1="0" x2="0" y2="1">
        <stop offset="0" stop-color="#7a5a3e"/>
        <stop offset="1" stop-color="#c9893f"/>
      </linearGradient>
      <linearGradient id="sewingPhoto" x1="0" y1="0" x2="1" y2="1">
        <stop offset="0" stop-color="#d8d6cf"/>
        <stop offset="1" stop-color="#6d6a63"/>
      </linearGradient>
    </defs>
    <path d="M0 0 H802 V392 Q560 400 300 432 Q140 452 0 452 Z" fill="url(#classPhoto)"/>
    <path d="M0 452 Q140 452 300 432 Q560 400 802 392 V410 Q560 418 300 450 Q140 470 0 470 Z" fill="var(--green-soft)"/>
    <path d="M0 452 Q140 452 300 432 Q560 400 802 392" fill="none" stroke="var(--white)" stroke-width="5"/>
    <circle cx="476" cy="400" r="78" fill="url(#worshipPhoto)" stroke="var(--white)" stroke-width="6"/>
    <circle cx="660" cy="372" r="104" fill="url(#sewingPhoto)" stroke="var(--white)" stroke-width="6"/>
  </svg>

  <h2 class="serve-heading">How We Serve</h2>

  <section class="service school">
    <h3><svg width="16" height="16" viewBox="0 0 16 16"><circle cx="8" cy="8" r="6.8" fill="none" stroke="var(--ink)" stroke-width="1.4"/><path d="M6.5 4.8 L9.7 8 L6.5 11.2" fill="none" stroke="var(--ink)" stroke-width="1.6"/></svg>Pre and Primary School</h3>
    <p>Our vision is to raise up a generation of godly influencers. Since the influencers in Tanzania speak English, our school is full-emersion English from K-7th grade. By graduation, our students are firmly grounded in their relationship with Christ. They receive the best education enabling them to take up positions of influence in every area of their nation. The 225 students also receive two nutritious meals every day, and health care.</p>
  </section>

  <section class="service kids">
    <h3><svg width="16" height="16" viewBox="0 0 16 16"><circle cx="8" cy="8" r="6.8" fill="none" stroke="var(--ink)" stroke-width="1.4"/><path d="M6.5 4.8 L9.7 8 L6.5 11.2" fill="none" stroke="var(--ink)" stroke-width="1.6"/></svg>Kids Club and Youth Camps</h3>
    <p>Kid's Clubs started as an outreach to children who survive on the streets. During the 2 hour weekly gatherings, the children receive food, play games, and learn everything from the most basic hygiene practices to the most-essential Word of God. This ministry has grown from 19 kids and 5 leaders in the first week, to over 1000 kids and more than 70 leaders in 14 different locations from Kigoma to almost 100 miles south on Lake Tanganyika.</p>
  </section>

  <section class="service village">
    <h3><svg width="16" height="16" viewBox="0 0 16 16"><circle cx="8" cy="8" r="6.8" fill="none" stroke="var(--ink)" stroke-width="1.4"/><path d="M6.5 4.8 L9.7 8 L6.5 11.2" fill="none" stroke="var(--ink)" stroke-width="1.6"/></svg>Village Outreaches</h3>
    <p>Our village outreaches are an exciting time to bring help and hope to remote villages along Lake Tanganyika and inland. We have seen much fruit from these outreaches over the years. A typical outreach consists of Kid's Clubs, door-to-door evangelism, seminars, Harvest Light Film at night, and even interviewing candidates for the Bible College. Several churches have also been planted.</p>
  </section>

  <section class="service trade">
    <h3><svg width="16" height="16" viewBox="0 0 16 16"><circle cx="8" cy="8" r="6.8" fill="none" stroke="var(--ink)" stroke-width="1.4"/><path d="M6.5 4.8 L9.7 8 L6.5 11.2" fill="none" stroke="var(--ink)" stroke-width="1.6"/></svg>Trade Schools</h3>
    <p>Jobs are hard to come by. However, through our Vocational Training Center, men and women are given the skills needed to help them support their families. Training has included sewing, jewelry making, bread baking, welding, concrete finishing, soap making, beauty salon, and business skills.</p>
  </section>

  <svg class="donate-band" viewBox="0 0 1200 932" aria-hidden="true">
    <path d="M868 826 Q1000 818 1200 812 V932 H846 Z" fill="var(--green-soft)"/>
    <path d="M880 834 Q1020 828 1200 824 V932 H858 Z" fill="var(--dark)"/>
  </svg>
  <div class="donate-title">Donate Now Change Lives</div>
  <div class="donate-site">
    <svg width="15" height="15" viewBox="0 0 16 16"><circle cx="8" cy="8" r="6.6" fill="none" stroke="var(--white)" stroke-width="1.3"/><ellipse cx="8" cy="8" rx="3" ry="6.6" fill="none" stroke="var(--white)" stroke-width="1.1"/><path d="M1.6 8 H14.4 M2.6 4.8 H13.4 M2.6 11.2 H13.4" stroke="var(--white)" stroke-width="1"/></svg>
    lampacrossborderstz-example.org
  </div>

</main>
</body>
</html>
```